Lumora Works - Design & Marketing Website Re-branding

UPDATE:
We are working on finalizing our color palette but are hoping that the designers will guide us to the right choice of colors by looking at our color inspiration file that we just uploaded and lead us in the right direction.

-----

I am exploring new design inspiration for a re-branding of my website. My current website is old and outdated and I lack the time to design it myself in addition to the fact that I am my own worst client.

I do website design, development and marketing as well as some SEO consulting and business development for small to mid-size companies in a range of industries.

https://lumoraworks.example

I like clean modern designs without cartoon images. The brands I'm going after are looking for a professional look and feel. I need something that shows my many years of being in business that is very professional.

I prefer minimal use of color. Mostly black and white with maybe one or two other colors. I am open to the suggestions by the designer.

Target Market(s)

Small to mid-size companies

Industry/Entity Type

Website Design, SEO and Markeitng

Number of Pages Required

4 page

Font styles to use
Sans Serif

Requirements
Must have
• Must be clean, modern and professional - I am not a huge fan of a lot of color and I'm open to new color suggestions by the designer
Nice to have
• A good balance of whitespace to content and graphics
Should not have
• Please no people illustrations

```html
<!DOCTYPE html>
<html lang="en">
<head>
<meta charset="utf-8">
<title>Lumora Works</title>
<link href="https://fonts.googleapis.com/css2?family=Poppins:wght@200;300;400;500;600&display=swap" rel="stylesheet">
<style>
:root{
  --ink:#1c1c1c;
  --black:#000;
  --paper:#f4f4f4;
  --white:#fff;
  --mauve:#b97aa9;
  --mute:#a9a9a9;
  --line:#9a9a9a;
}
*{box-sizing:border-box;margin:0;padding:0}
html,body{width:813px;height:1200px;overflow:hidden;background:#e9e9e9;font-family:'Poppins',sans-serif;color:var(--ink)}
.page{position:absolute;left:154px;top:0;width:978px;height:2324px;background:var(--paper);transform:scale(0.5164);transform-origin:0 0;overflow:hidden}
.abs{position:absolute}
.header{left:0;top:0;width:978px;height:61px;background:var(--black)}
.brand-name{left:42px;top:17px;color:var(--white);font-weight:600;font-size:20px;line-height:26px}
.nav{right:43px;top:22px;display:flex;gap:18px;font-size:11px;color:var(--white)}
.hero-title{left:0;top:140px;width:978px;text-align:center;font-size:42px;font-weight:600;line-height:49px}
.hero-sub{left:0;top:278px;width:978px;text-align:center;font-size:22px;font-weight:300;line-height:26px}
.btn{height:30px;border-radius:2px;font-size:11px;display:flex;align-items:center;justify-content:center}
.btn-fill{background:var(--mauve);color:var(--white)}
.btn-line{border:1px solid var(--line);background:var(--white);color:var(--ink)}
.card{top:478px;height:171px;border-radius:8px;overflow:hidden}
.card-a{left:117px;width:289px;background:var(--white)}
.card-a .name{position:absolute;top:20px;width:100%;text-align:center;font-weight:600;font-size:20px;color:#6b2b1e}
.card-a .tag{position:absolute;top:62px;width:100%;text-align:center;font-weight:300;font-size:15px;color:#6b2b1e}
.card-a .photos{position:absolute;left:0;top:95px;width:289px;height:76px;background:linear-gradient(90deg,#7a5a48,#b09280 40%,#4f5d6b)}
.card-b{left:420px;width:289px;background:linear-gradient(135deg,#b8ada8,#7d6b73 50%,#5d4d62)}
.card-b .name{position:absolute;left:22px;top:16px;font-size:30px;font-weight:300;color:#4a4040}
.card-c{left:724px;width:290px;background:linear-gradient(135deg,#f3f1cf,#e4f2e6)}
.card-c .name{position:absolute;left:40px;top:52px;font-size:36px;font-weight:600;color:#e7a98b}
.card-c .tag{position:absolute;left:41px;top:99px;font-size:12px;color:#a9d1c8}
.arrows{left:872px;top:662px;display:flex;gap:30px}
.section-title{left:0;width:978px;text-align:center;font-size:22px;font-weight:600}
.para{left:150px;width:678px;text-align:center;font-size:11px;line-height:16px}
.feature h3{font-size:21px;font-weight:500;margin-bottom:24px;white-space:nowrap}
.feature p{font-size:11px;line-height:16px}
.logo-row{top:1222px;left:42px;width:894px;display:flex;justify-content:space-between;align-items:center;height:40px}
.logo-row span{font-size:24px;font-weight:600;color:var(--mute);display:flex;align-items:center;gap:8px}
.logo-row b{display:inline-block;width:26px;height:26px;border-radius:50%;border:3px solid #d4d4d4}
.service .num{font-size:44px;font-weight:200;color:var(--ink);line-height:44px;height:48px}
.service h3{font-size:21px;font-weight:500;margin:8px 0 12px 3px;white-space:nowrap}
.service p{font-size:11px;line-height:16px;height:42px}
.service .btn{width:176px}
.band{left:0;top:1661px;width:978px;height:414px;background:linear-gradient(120deg,#d8d6d6,#c9c0bc 35%,#d4cbc6 60%,#cdc8c9)}
.band-title{left:0;top:1762px;width:978px;text-align:center;font-size:22px;font-weight:600}
.band-text{left:210px;top:1843px;width:580px;text-align:center;font-size:11px;line-height:16px}
.footer{left:0;top:2075px;width:978px;height:249px;background:var(--black);color:var(--white)}
.f-brand{left:102px;top:60px;font-size:18px;font-weight:500}
.f-social{left:104px;top:96px;display:flex;gap:22px}
.f-social i{width:13px;height:13px;border-radius:50%;background:var(--white);display:block}
.f-links{left:343px;top:64px;display:flex;gap:37px;font-size:11px}
.f-cta{left:646px;top:64px;width:230px;font-size:11px;line-height:16px}
.f-cta strong{font-weight:600;display:block;margin-bottom:6px}
.f-phone{display:flex;align-items:center;gap:10px;margin-top:5px}
.f-copy{left:0;top:207px;width:978px;text-align:center;font-size:10px}
</style>
</head>
<body>
<div class="page">
  <header class="abs header">
    <div class="abs brand-name">Lumora Works</div>
    <nav class="abs nav"><span>Simplify</span><span>Design</span><span>Connect</span><span>About</span></nav>
  </header>

  <h1 class="abs hero-title">Every business has a story.<br>We help you tell it.</h1>
  <p class="abs hero-sub">Compelling website experiences that<br>elevate your business.</p>
  <a class="abs btn btn-fill" style="left:309px;top:373px;width:172px">Let's Chat</a>
  <a class="abs btn btn-line" style="left:496px;top:373px;width:174px">What we do</a>

  <div class="abs card card-a">
    <div class="name">Kestrel Ventures</div>
    <div class="tag">Backing bold founders.</div>
    <div class="photos" role="img" aria-label="Row of team photographs"></div>
  </div>
  <div class="abs card card-b" role="img" aria-label="Food photograph of pancakes with berry compote">
    <div class="name">Harbor Table</div>
  </div>
  <div class="abs card card-c">
    <div class="name">Brightpath</div>
    <div class="tag">Where Teams Grow Together</div>
  </div>
  <div class="abs arrows">
    <svg width="18" height="18" viewBox="0 0 18 18"><path d="M15 9H3M8 4L3 9l5 5" fill="none" stroke="#111" stroke-width="2"/></svg>
    <svg width="18" height="18" viewBox="0 0 18 18"><path d="M3 9h12M10 4l5 5-5 5" fill="none" stroke="#111" stroke-width="2"/></svg>
  </div>

  <h2 class="abs section-title" style="top:778px">We create websites that inspire</h2>
  <p class="abs para" style="top:850px">We are a collaborative team of word nerds, choreographers of shapes &amp; ideas, ambassadors of data, content warriors and inspirational conversationalists ready to help you no matter where you are in your journey.</p>
  <p class="abs para" style="top:914px">We have a deep understanding of what it takes to grow a business and we collaborate with you every step of the way from strategy to implementation and beyond.</p>

  <div class="abs feature" style="left:116px;top:1025px;width:240px"><h3>Proven process</h3><p>We have carefully crafted each step in our process for successful outcomes.</p></div>
  <div class="abs feature" style="left:388px;top:1025px;width:200px"><h3>Connection</h3><p>We take the time to truly listen and understand your audience and business needs.</p></div>
  <div class="abs feature" style="left:621px;top:1025px;width:210px"><h3 style="margin-left:5px">Exceeding your goals</h3><p>We develop actionable strategies for success based on your unique goals.</p></div>

  <div class="abs logo-row">
    <span><b></b>Keystone</span>
    <span>Harbor Table</span>
    <span>Snapwise</span>
    <span>Brightpath</span>
    <span>CapLink</span>
  </div>

  <div class="abs service" style="left:80px;top:1404px;width:260px">
    <div class="num">1</div><h3>Websites Simplified</h3>
    <p>A complete end-to-end website subscription solution that propels your business forward.</p>
    <a class="btn btn-fill">Complete Website Solution</a>
  </div>
  <div class="abs service" style="left:376px;top:1404px;width:280px">
    <div class="num">2</div><h3>Custom Website Design</h3>
    <p>Blending the best principles of design, data and functionality to express your brand.</p>
    <a class="btn btn-fill">Design Services</a>
  </div>
  <div class="abs service" style="left:700px;top:1404px;width:210px">
    <div class="num">3</div><h3>Website Support</h3>
    <p>Reliable top tier managed website support, maintenance and hosting.</p>
    <a class="btn btn-fill">Website Care</a>
  </div>

  <div class="abs band" role="img" aria-label="Photograph of team hands joined over a meeting table"></div>
  <h2 class="abs band-title">Working with us...</h2>
  <p class="abs band-text">Our team is well-versed in the latest web design trends and technologies, and utilize our expertise to deliver cutting-edge designs that will help your business stand out in the crowded online market.</p>
  <a class="abs btn btn-fill" style="left:405px;top:1931px;width:172px">Let's Work Together</a>

  <footer class="abs footer">
    <div class="abs f-brand">lumoraworks</div>
    <div class="abs f-social"><i></i><i></i><i></i><i></i></div>
    <div class="abs f-links"><span>Privacy</span><span>Terms</span><span>Disclaimer</span></div>
    <div class="abs f-cta">
      <strong>Need to bounce ideas around?</strong>
      Hit us up for a quick 15-minute call and let's hash it out.
      <div class="f-phone"><svg width="12" height="12" viewBox="0 0 24 24"><path fill="#fff" d="M6.6 10.8a15 15 0 0 0 6.6 6.6l2.2-2.2c.3-.3.7-.4 1-.2 1.1.4 2.3.6 3.6.6.6 0 1 .4 1 1V20c0 .6-.4 1-1 1A17 17 0 0 1 3 4c0-.6.4-1 1-1h3.5c.6 0 1 .4 1 1 0 1.3.2 2.5.6 3.6.1.3 0 .7-.2 1z"/></svg>555-014-2290</div>
    </div>
    <div class="abs f-copy">© 2024 Lumora Works, LLC. All Rights Reserved.</div>
  </footer>
</div>
</body>
</html>
```